SPICE LABEL DESIGN FOR A TASTY DRY RUB! (chicken, ribs, wings)

Looking for a fun/creative/edgy label for a spice jar! The label will be rectangular (exact size tbd - but approximately 1.2" W X 3" H).
This spice is a dry rub blend of 14 EPIC spices, to be used on chicken, chicken wings, ribs, etc.
Copywritting on the label to be;
Tova JK's Blaze BBQ Rub
A blend of 14 UNTOVAGETTABLE spices
*Note the word "untovagettabe" is spelt incorectly on purpose for a play a words with "tova". Please use a different color font for "tova" within the word.
Also would like "Tova JK's" to be prominent
Looking for an illustration/design that is fun/creative/catchy/edgy/appealing! While still keeping the design appealing to higher end markets. Have fun with it and think outside of the box!! :)
People who enjoy cooking, young adults and adults, display at restaurants or retail markets

```html
<!DOCTYPE html>
<html lang="en">
<head>
<meta charset="utf-8">
<title>Tova JK's Blaze BBQ Rub – Spice Label</title>
<link rel="stylesheet" href="https://fonts.googleapis.com/css2?family=Alfa+Slab+One&family=Oswald:wght@700&family=Ultra&display=swap">
<style>
  :root {
    --bg-dark: #141010;
    --bg-warm: #231414;
    --pattern-red: #3a1515;
    --brand-gold: #f6a623;
    --flame-orange: #ff5b1f;
    --ribbon-red: #d4121d;
    --ribbon-shadow: #8e0a12;
    --rub-red: #e2162c;
    --plate-red: #d3141d;
    --plate-deep: #a80c15;
    --ink-black: #111111;
    --blush: #ffc6ae;
    --spice-light: #d98a45;
    --spice-deep: #9b4a1c;
  }
  html, body {
    margin: 0;
    padding: 0;
    width: 1200px;
    height: 3000px;
    overflow: hidden;
    background: var(--bg-dark);
  }
  .label {
    position: relative;
    width: 1200px;
    height: 3000px;
    overflow: hidden;
    background: radial-gradient(ellipse at 50% 30%, var(--bg-warm) 0%, var(--bg-dark) 70%);
  }
  .background-pattern {
    position: absolute;
    inset: 0;
    background: linear-gradient(160deg, rgba(58,21,21,0.35) 0%, rgba(20,16,16,0) 45%, rgba(58,21,21,0.3) 100%);
  }
  .label-art {
    position: absolute;
    inset: 0;
    width: 1200px;
    height: 3000px;
  }
  .brand-name { font-family: "Alfa Slab One", serif; fill: var(--brand-gold); }
  .headline-blaze { font-family: "Oswald", sans-serif; font-weight: 700; fill: var(--flame-orange); }
  .ribbon-text { font-family: "Ultra", serif; fill: var(--ink-black); }
  .headline-rub { font-family: "Ultra", serif; fill: var(--rub-red); }
  .tagline { font-family: "Alfa Slab One", serif; fill: var(--blush); }
  .tagline-accent { fill: var(--brand-gold); }
  .tagline-highlight { fill: var(--brand-gold); }
  .tagline-name { fill: var(--blush); }
</style>
</head>
<body>
<main class="label">
  <div class="background-pattern" role="img" aria-label="Faint dark red line pattern of grilling and food doodles"></div>

  <svg class="label-art" viewBox="0 0 1200 3000" xmlns="http://www.w3.org/2000/svg">
    <defs>
      <radialGradient id="plateGradient" cx="50%" cy="30%" r="70%">
        <stop offset="0%" stop-color="var(--plate-red)"/>
        <stop offset="100%" stop-color="var(--plate-deep)"/>
      </radialGradient>
      <linearGradient id="spiceGradient" x1="0" y1="0" x2="0" y2="1">
        <stop offset="0%" stop-color="var(--spice-light)"/>
        <stop offset="100%" stop-color="var(--spice-deep)"/>
      </linearGradient>
    </defs>

    <!-- Brand name -->
    <text class="brand-name" x="600" y="318" text-anchor="middle" font-size="178" textLength="930" lengthAdjust="spacingAndGlyphs">TOVA JK'S</text>

    <!-- Headline -->
    <text class="headline-blaze" x="600" y="945" text-anchor="middle" font-size="470" textLength="980" lengthAdjust="spacingAndGlyphs">BLAZE</text>

    <!-- Ribbon banner -->
    <g class="ribbon">
      <polygon points="80,995 200,995 200,1175 80,1175 125,1085" fill="var(--ribbon-shadow)"/>
      <polygon points="1120,995 1000,995 1000,1175 1120,1175 1075,1085" fill="var(--ribbon-shadow)"/>
      <rect x="150" y="965" width="900" height="200" fill="var(--ribbon-red)"/>
      <line x1="175" y1="988" x2="1025" y2="988" stroke="var(--ink-black)" stroke-width="6"/>
      <line x1="175" y1="1142" x2="1025" y2="1142" stroke="var(--ink-black)" stroke-width="6"/>
      <text class="ribbon-text" x="600" y="1122" text-anchor="middle" font-size="160" textLength="500" lengthAdjust="spacingAndGlyphs">BBQ</text>
    </g>

    <text class="headline-rub" x="600" y="1568" text-anchor="middle" font-size="400" textLength="900" lengthAdjust="spacingAndGlyphs">RUB</text>

    <!-- Red plate -->
    <circle cx="600" cy="2844" r="1144" fill="url(#plateGradient)"/>

    <!-- Spice mound -->
    <path role="img" aria-label="Photograph of a heaped pile of orange-red BBQ dry rub"
          d="M0,2230 C120,2080 330,1870 560,1820 C760,1790 960,1900 1200,2040 L1200,2290 C900,2340 400,2345 0,2300 Z"
          fill="url(#spiceGradient)"/>

    <!-- Tagline -->
    <text class="tagline" x="600" y="2580" text-anchor="middle" font-size="112" textLength="1000" lengthAdjust="spacingAndGlyphs">A BLEND OF <tspan class="tagline-accent">14</tspan></text>
    <text class="tagline tagline-highlight" x="600" y="2728" text-anchor="middle" font-size="112" textLength="1040" lengthAdjust="spacingAndGlyphs">UN<tspan class="tagline-name">TOVA</tspan>GETTABLE</text>
    <text class="tagline" x="600" y="2870" text-anchor="middle" font-size="112" textLength="470" lengthAdjust="spacingAndGlyphs">SPICES</text>
  </svg>
</main>
</body>
</html>
```